A Dedicated Thank You to my Dad

Proposed Dimensions: Approx. 20" x 30"

For Father's Day, I wrote a dedication to my Dad that encapsulates my gratitude for everything he does, and everything he is. His birthday is on August 3, but it is more important for me to transform this dedication into a meaningful and memorable gift than to meet any deadline. I would love an image that captures the relationship between a father and his son, accompanied by my words of thanks in some sort of font that is appropriate for the message (calligprahy? not sure about that).

I had actually posted the Thank You on Pixelmarrow as a public post, so anyone with an account can read it: https://www.pixelmarrow.example/photo.php?fbid=40872219360548813&set=a.318760942157.6650129.3908471&type=1&theater

Only the words starting with "Thank you ..." should be on the poster.

Target Market(s)

This is a personal gift for my Dad. He doesn't have the best of eyesight, so having the words in a really small font would not be particularly helpful. :-)

Requirements
Must have
• * Personable
* Warm
* Inviting
* Memorable
* Understated more favored over Loud
Should not have
• * An entire palette of colors
* Wacky colors or fonts

```html
<!DOCTYPE html>
<html lang="en">
<head>
<meta charset="utf-8">
<title>For my Dad, Walter Brennick</title>
<link rel="stylesheet" href="https://fonts.googleapis.com/css2?family=Cinzel:wght@400;500&display=swap">
<style>
  :root {
    --backdrop: #d3d4d6;
    --paper: #ffffff;
    --ink: #3a3a3a;
    --field-gold: #c9a878;
    --field-brown: #6e5a44;
    --haze-lilac: #b7a3b4;
    --haze-light: #efe6dc;
  }
  * { margin: 0; padding: 0; box-sizing: border-box; }
  html, body {
    width: 1200px;
    height: 1008px;
    overflow: hidden;
    background: var(--backdrop);
  }
  .canvas {
    position: relative;
    width: 1200px;
    height: 1008px;
  }
  .poster {
    position: absolute;
    left: 280px;
    top: 38px;
    width: 622px;
    height: 932px;
    background: var(--paper);
    overflow: hidden;
  }
  .poster__photo {
    position: absolute;
    left: 0;
    right: 0;
    bottom: 0;
    height: 330px;
    background:
      radial-gradient(ellipse 60% 45% at 40% 85%, rgba(110, 90, 68, 0.75), rgba(110, 90, 68, 0) 70%),
      linear-gradient(180deg,
        rgba(255, 255, 255, 1) 0%,
        rgba(239, 230, 220, 0.9) 25%,
        rgba(183, 163, 180, 0.75) 50%,
        rgba(201, 168, 120, 0.9) 75%,
        var(--field-brown) 100%);
  }
  .poster__text {
    position: relative;
    padding: 14px 20px 0 32px;
    font-family: "Cinzel", serif;
    color: var(--ink);
  }
  .poster__title {
    font-size: 16.5px;
    font-weight: 400;
    letter-spacing: 0.3px;
    margin-bottom: 23px;
  }
  .poster__thanks {
    list-style: none;
    font-size: 12.6px;
    line-height: 17.2px;
    text-transform: uppercase;
  }
  .poster__thanks li { margin: 0; }
</style>
</head>
<body>
<div class="canvas">
  <article class="poster">
    <div class="poster__photo" role="img" aria-label="Soft-focus photograph of a father and son in a sunlit golden field"></div>
    <div class="poster__text">
      <h1 class="poster__title">For my Dad, Walter Brennick</h1>
      <ul class="poster__thanks">
        <li>Thank you for, after the initial shock, embracing the unexpected news that you were about to have twins.</li>
        <li>Thank you for buying enough diapers to single-handedly enable K &amp; L to make a profit.</li>
        <li>Thank you for always carrying us to the car after we fell asleep, even after we were definitely old enough to walk it.</li>
        <li>Thank you for not telling on us when we were only pretending to nap.</li>
        <li>Thank you for welcoming more people to stay with us than I can count.</li>
        <li>Thank you for sitting through more showings of “Jukebox Summer” and “Comet Raiders” than any human should endure.</li>
        <li>Thank you for doggedly trying to teach me that the beach is not to be feared nor cleaned.</li>
        <li>Thank you for working two jobs, for years, to make ends meet.</li>
        <li>Thank you for loading us all up in the station wagon, pillows in tow, so we could watch the first drive-in movie together and squint in the second.</li>
        <li>Thank you for, as coach, letting me take a fake rabbit’s foot onto the soccer field.</li>
        <li>Thank you for being willing to put a hit out on my guitar teacher when he beat feet.</li>
        <li>Thank you for letting me sing in my room as if I were the originating artist.</li>
        <li>Thank you for making car trips with you, wherever we were going, fun and special.</li>
        <li>Thank you for proudly and patiently taking me to my first nerd conference in junior high.</li>
        <li>Thank you for putting up with the commutes you did, for decades, so we could grow up amongst family in an incredible community.</li>
        <li>Thank you for my dry sense of humor. I cherish it.</li>
        <li>Thank you for finding a way, by hook or by crook, to send three children to college at the same time, and to allow me to go to the college of my dreams.</li>
        <li>Thank you for never giving up on trying to convince me that imperfection is not a failure.</li>
        <li>Thank you for mispronouncing, I believe on purpose, pop culture references in a way that only you can.</li>
        <li>Thank you for teaching me to try to find the good in everyone.</li>
        <li>Thank you for waiting to laugh out loud with Mom until after the police left when my camp friends and I apparently made too much noise.</li>
        <li>Thank you for showing me that there is peace to be found in stillness and quiet.</li>
        <li>Thank you for demonstrating the fun that can be had and the truths that can be gleaned from philosophical and political debate.</li>
        <li>Thank you for accepting me for who I am, no matter who I love, and for helping me to accept myself.</li>
        <li>Thank you for doing whatever you can to help whoever you can, whether friend, family or stranger.</li>
        <li>Thank you for trusting me enough to let your guard sometimes to let me know how you are truly doing.</li>
        <li>Thank you for insisting, year after year, that time with you means more than any gift I could ever purchase. That is one lesson, amongst so many, that I will pass down to our next generation.</li>
      </ul>
    </div>
  </article>
</div>
</body>
</html>
```